Super elegant, crisp & clean Business card design required

We recently upgraded our branding - which is on our website - tavorelstudio.com

I would like a simple, yet elegant, clean business card design please.

The font of my logo is Cinzel - and because of the natural colour - it's best to have this on a black background.

I would like to have the back of the business card - with simply my logo.

PLEASE DO NOT SUBMIT A COMPLICATED / UNCLEAN DESIGN

Industry/Entity Type

Business

Contact Information for Business Card

Dalvik Ostrander Photography

Font styles to use
Other font styles liked:
• Cinzel

Requirements
Must have
• A backpage with nothing but my logo
• Simple design - stands out
Should not have
• Colour that dont align with my logo
• Over complicated '/ non symmetrical design

```html
<!DOCTYPE html>
<html lang="en">
<head>
<meta charset="utf-8">
<title>Dalvik Ostrander Photography — Business Card</title>
<link href="https://fonts.googleapis.com/css2?family=Cinzel:wght@400;700&display=swap" rel="stylesheet">
<style>
  :root {
    --backdrop: #2a2a2b;
    --card-black: #050505;
    --card-white: #ffffff;
    --gold: #8f7d62;
    --ink: #111111;
    --muted: #6b6b6b;
    --rule: #1a1a1a;
  }
  * { margin: 0; padding: 0; box-sizing: border-box; }
  html, body {
    width: 1200px; height: 900px; overflow: hidden;
    background: var(--backdrop);
    font-family: "Cinzel", serif;
  }
  .canvas {
    position: relative; width: 1200px; height: 900px;
  }
  .card {
    position: absolute;
    width: 560px; height: 320px;
    border-radius: 22px;
    box-shadow: 0 12px 30px rgba(0,0,0,0.45);
  }
  /* Back of card */
  .card--back {
    left: 320px; top: 100px;
    background: var(--card-black);
    display: flex; flex-direction: column; align-items: center; justify-content: center;
    color: var(--gold);
  }
  .brand-mark__name {
    font-size: 30px; font-weight: 400; letter-spacing: 1px;
  }
  .brand-mark__sub {
    margin-top: 4px; font-size: 12px; font-weight: 400; letter-spacing: 7px;
  }
  /* Front of card */
  .card--front {
    left: 320px; top: 480px;
    background: var(--card-white);
    display: flex; align-items: center;
  }
  .front__brand {
    width: 250px; display: flex; justify-content: center;
    color: var(--gold); font-size: 22px; font-weight: 400; text-align: center; line-height: 1.25;
  }
  .front__divider {
    width: 2px; height: 104px; background: var(--rule);
  }
  .front__details { padding-left: 24px; }
  .holder__name {
    font-size: 22px; font-weight: 700; color: var(--ink); letter-spacing: 0.5px;
  }
  .holder__role {
    font-size: 14px; color: var(--gold); letter-spacing: 0.5px; margin-bottom: 10px;
  }
  .contact-list { list-style: none; }
  .contact-list__item {
    display: flex; align-items: center; gap: 10px;
    font-size: 13px; color: var(--ink); line-height: 22px;
  }
  .contact-list__icon { width: 12px; height: 12px; flex: none; }
</style>
</head>
<body>
<main class="canvas">
  <section class="card card--back" aria-label="Card back">
    <div class="brand-mark__name">Dalvik Ostrander</div>
    <div class="brand-mark__sub">PHOTOGRAPHY</div>
  </section>

  <section class="card card--front" aria-label="Card front">
    <div class="front__brand">Dalvik<br>Ostrander</div>
    <div class="front__divider"></div>
    <div class="front__details">
      <div class="holder__name">Dalvik Ostrander</div>
      <div class="holder__role">Photography</div>
      <ul class="contact-list">
        <li class="contact-list__item">
          <svg class="contact-list__icon" viewBox="0 0 12 12"><path d="M2.5 1 L4.5 1 L5.2 3.6 L4 4.6 Q5 7 7.4 8 L8.4 6.8 L11 7.5 L11 9.5 Q10.5 11 9 11 Q1 10 1 2.5 Q1 1 2.5 1Z" fill="#6b6b6b"/></svg>
          +330 5172-4093
        </li>
        <li class="contact-list__item">
          <svg class="contact-list__icon" viewBox="0 0 12 12"><rect x="1" y="2.5" width="10" height="7" fill="none" stroke="#6b6b6b" stroke-width="1.2"/><path d="M1 2.5 L6 6.5 L11 2.5" fill="none" stroke="#6b6b6b" stroke-width="1.2"/></svg>
          info@tavorelstudio.com
        </li>
        <li class="contact-list__item">
          <svg class="contact-list__icon" viewBox="0 0 12 12"><circle cx="6" cy="6" r="5" fill="none" stroke="#6b6b6b" stroke-width="1.1"/><ellipse cx="6" cy="6" rx="2.2" ry="5" fill="none" stroke="#6b6b6b" stroke-width="1"/><path d="M1 6 H11" stroke="#6b6b6b" stroke-width="1"/></svg>
          www.tavorelstudio.com
        </li>
      </ul>
    </div>
  </section>
</main>
</body>
</html>
```